Design a double sided business card

We are looking for a clean, eye-catching, and contemporary design that enhances the brand and presents a premium, professional image. Our preference is for a brown card with black gloss detailing and embossed elements; however, we are open to creative input and design suggestions that best achieve a strong visual impact.

Please see the attached existing business card for reference. We use both black and brown colours consistently across our branding.

On sample provided

```html
<!DOCTYPE html>
<html lang="en">
<head>
<meta charset="utf-8">
<title>Korvan – Business Card</title>
<link href="https://fonts.googleapis.com/css2?family=Quicksand:wght@400;500;700&display=swap" rel="stylesheet">
<style>
  :root {
    --page-bg: #ece8e3;
    --card-beige: #d9ccbd;
    --card-beige-dark: #cbbba8;
    --ink: #1c1c1e;
    --ink-soft: #3a3836;
    --photo-light: #b7c8dc;
    --photo-mid: #b9b6b1;
    --photo-dark: #7d6e66;
  }
  * { margin: 0; padding: 0; box-sizing: border-box; }
  html, body { width: 1200px; height: 913px; overflow: hidden; }
  body {
    background: var(--page-bg);
    font-family: "Quicksand", sans-serif;
    color: var(--ink);
    position: relative;
  }
  .card {
    position: absolute;
    width: 540px;
    height: 310px;
    border-radius: 4px;
    overflow: hidden;
    box-shadow: 0 10px 28px rgba(0,0,0,0.18);
  }
  /* Front */
  .card-front {
    left: 50px; top: 100px;
    background: linear-gradient(135deg, var(--card-beige) 0%, var(--card-beige-dark) 100%);
  }
  .card-front .wordmark {
    position: absolute; left: 58px; top: 92px;
    font-weight: 700; font-size: 54px; letter-spacing: 10px;
    color: var(--ink);
  }
  .card-front .rule {
    position: absolute; left: 150px; top: 182px;
    width: 350px; height: 1px; background: var(--ink-soft);
  }
  .person { position: absolute; left: 40px; top: 170px; }
  .person .name { font-size: 17px; font-weight: 500; letter-spacing: 0.5px; }
  .person .role { font-size: 13px; color: var(--ink-soft); margin-top: 1px; }
  .contacts { position: absolute; left: 40px; top: 222px; list-style: none; }
  .contacts li {
    display: flex; align-items: center; gap: 8px;
    font-size: 14px; color: var(--ink-soft); line-height: 22px;
  }
  .contacts svg { width: 13px; height: 13px; }
  .address {
    position: absolute; right: 34px; top: 200px;
    text-align: right; font-size: 13px; line-height: 18px; color: var(--ink-soft);
  }
  .card-front .edge {
    position: absolute; right: 0; bottom: 0; width: 100%; height: 5px;
    background: var(--ink);
  }
  /* Back */
  .card-back { left: 610px; top: 490px; }
  .card-back .photo {
    position: absolute; inset: 0;
    background: linear-gradient(170deg, var(--photo-light) 0%, var(--photo-mid) 55%, var(--photo-dark) 100%);
  }
  .brand-lockup {
    position: absolute; left: 44px; top: 108px;
    display: flex; align-items: center; gap: 22px;
  }
  .brand-lockup .mark {
    width: 56px; height: 56px; border: 5px solid var(--ink);
  }
  .brand-lockup .divider { width: 2px; height: 64px; background: var(--ink); }
  .brand-lockup .wordmark {
    font-weight: 700; font-size: 48px; letter-spacing: 9px; color: var(--ink);
  }
  .website {
    position: absolute; left: 150px; top: 76px;
    font-size: 15px; font-weight: 700; letter-spacing: 1px; color: var(--ink);
  }
</style>
</head>
<body>
  <section class="card card-front">
    <div class="wordmark">KORVAN</div>
    <div class="rule"></div>
    <div class="person">
      <div class="name">DARA PELL</div>
      <div class="role">Director</div>
    </div>
    <ul class="contacts">
      <li><svg viewBox="0 0 13 13"><rect x="3" y="0.5" width="7" height="12" rx="1" fill="none" stroke="#3a3836"/></svg>07700900123</li>
      <li><svg viewBox="0 0 13 13"><path d="M3 1 L5 4 L4 5.5 Q5.5 8 7.5 9 L9 8 L12 10 L10.5 12 Q3 11 1 2.5 Z" fill="#3a3836"/></svg>0800 000 4417</li>
      <li><svg viewBox="0 0 13 13"><rect x="0.5" y="2.5" width="12" height="8" fill="#3a3836"/><path d="M0.5 2.5 L6.5 7 L12.5 2.5" fill="none" stroke="#d9ccbd"/></svg>dara@korvan.co.uk</li>
    </ul>
    <div class="address">The Green Mill Lane<br>Eastfield AB1 2CD</div>
    <div class="edge"></div>
  </section>

  <section class="card card-back">
    <div class="photo" role="img" aria-label="Photograph of a modern flat-roofed building with glass walls under a blue sky with bare trees"></div>
    <div class="website">www.korvan.co.uk</div>
    <div class="brand-lockup">
      <div class="mark"></div>
      <div class="divider"></div>
      <div class="wordmark">KORVAN</div>
    </div>
  </section>
</body>
</html>
```